A WEBSITE FOR A JEWELLERY RETAIL STORE WITH A SHOPPING CART, AND ABILITY TO ORDER ONLINE.

I require a website with a shopping cart.

We sell MAINLY diamond jewellery (such as rings etc). I need it to be simple to change prices with only a few buttons, as the price fluctuates due to the US Dollar.

We are a diamond wholesaler, selling directly to the public, so we guarantee the lowest prices in Australia.

There is also a link to current inventory that will need to be uploaded to the site.

This could be an ongoing job, where you will be paid weekly to maintain and update the website if you wish.

Target Market(s)

People getting engaged, and wanting to buy a diamond ring.

Number of Pages Required

5+ page

Colors

Designer to choose colors to be used in the design.

Requirements
Must have
• elegant.
• modern.
• professional.
• SHOPPING CART.
• ABILITY TO SEARCH FOR LOOSE DIAMONDS (LINK THAT NEEDS TO BE EMBEDDED WILL BE SENT WHICH SHOWS CURRENT STOCK).
• ENGAGEMENT RINGS
• WEDDING RINGS
• DIAMOND EARRINGS
• DIAMOND PENDANTS
• LOOSE DIAMONDS.
• SALE ITEMS.
• OTHER JEWELLERY.
• EDUCATION
• WISH LIST
• CART.
Nice to have
• a good place to look for inspiration on pages is https://www.lumenvael.example.
• YOU MAY VISIT OUR FACEBOOK PAGE AT.
• HTTP://WWW.SOCIALPAGE.EXAMPLE/QUILLSTONEJEWELLERS
Should not have
• We don't want it too busy.

```html
<!DOCTYPE html>
<html lang="en">
<head>
<meta charset="utf-8">
<title>Quillstone Jewellers</title>
<link rel="stylesheet" href="https://fonts.googleapis.com/css2?family=Questrial&display=swap">
<style>
:root{
  --ink:#1a1a1a;
  --black:#000;
  --white:#fff;
  --line:#cfcfcf;
  --muted:#666;
  --soft:#f3f3f3;
  --dark-band:#141414;
  --star:#e8c34a;
}
*{box-sizing:border-box;margin:0;padding:0}
html,body{width:1200px;height:4138px;overflow:hidden}
body{position:relative;background:var(--white);color:var(--ink);font-family:"Questrial",sans-serif}
h1,h2,h3{font-weight:400}
.abs{position:absolute}
.btn{position:absolute;display:flex;align-items:center;justify-content:center;border:1.5px solid currentColor;font-size:13px;letter-spacing:1px;text-transform:uppercase}
.section-title{position:absolute;left:0;width:1200px;text-align:center;font-size:27px;letter-spacing:2px;text-transform:uppercase}

/* header */
.site-header{top:0;left:0;width:1200px;height:83px;background:var(--white);border-bottom:1px solid #eee}
.menu{left:118px;top:30px;display:flex;align-items:center;gap:10px;font-size:15px;letter-spacing:1px}
.menu svg{display:block}
.brand{left:0;width:1200px;top:18px;display:flex;justify-content:center;align-items:center;gap:10px}
.brand-mark{width:20px;height:20px;background:var(--black)}
.brand-name{font-size:22px;letter-spacing:2px;text-transform:uppercase;line-height:1.05;text-align:center}
.header-icons{right:118px;top:30px;display:flex;gap:26px}

/* hero */
.hero{top:83px;left:0;width:1200px;height:634px;background:radial-gradient(ellipse at 55% 40%,#5a5a5a 0%,#2a2a2a 45%,#0e0e0e 100%)}
.hero-gems{left:560px;top:150px;width:560px;height:470px;border-radius:50%;background:radial-gradient(circle,#f4f4f4 0%,#b9b9b9 45%,rgba(60,60,60,0) 72%)}
.hero-frame{left:124px;top:262px;width:410px;height:180px;border:1.5px solid rgba(255,255,255,.8);color:var(--white);text-align:center;padding-top:10px}
.hero-frame .kicker{font-size:22px;letter-spacing:2px;background:#2a2a2a;display:inline-block;padding:0 10px;margin-top:-26px;position:relative;top:-2px}
.hero-frame .headline{font-size:40px;letter-spacing:2px;line-height:1.05}
.hero-frame .amp{font-size:26px;line-height:1}
.hero .btn{left:245px;top:455px;width:156px;height:45px;color:var(--white)}

/* explore */
.explore-title{top:762px}
.category{top:820px;width:240px;text-align:center}
.category .thumb{width:150px;height:150px;margin:0 auto;border-radius:50%;background:radial-gradient(circle,#e6e6e6 0%,#f6f6f6 60%,#fff 100%)}
.category .label{margin-top:24px;font-size:17px;letter-spacing:1.5px;text-transform:uppercase}

/* featured */
.feature-title{top:1127px}
.tabs{left:0;width:1200px;top:1210px;display:flex;justify-content:center;gap:24px;font-size:13px;text-transform:uppercase;color:var(--muted)}
.tabs .active{color:var(--ink);border-bottom:1.5px solid var(--ink);padding-bottom:8px}
.tabs-line{left:402px;top:1236px;width:396px;height:1px;background:var(--line)}
.pager{left:1024px;top:1205px;font-size:24px;color:#999;letter-spacing:6px}
.product{top:1288px;width:300px;height:410px;border:1.5px solid var(--line);text-align:center}
.product .tag{position:absolute;left:0;top:0;width:34px;height:108px;background:var(--black);color:var(--white);font-size:14px;writing-mode:vertical-rl;transform:rotate(180deg);display:flex;align-items:center;justify-content:center;letter-spacing:1px}
.product .photo{width:190px;height:150px;margin:38px auto 0;border-radius:40%;background:radial-gradient(ellipse,#dcdcdc 0%,#f4f4f4 55%,#fff 100%)}
.product .name{margin-top:50px;font-size:22px;text-transform:uppercase;letter-spacing:1px}
.product .rule{width:220px;height:1px;background:var(--line);margin:20px auto 22px}
.product .price{font-size:22px}
.browse{left:521px;top:1757px;width:158px;height:45px;color:var(--ink)}

/* offer */
.offer{top:1857px;left:0;width:1200px;height:386px;background:linear-gradient(100deg,#1c1c1c 0%,#2e2e2e 40%,#3c3c3c 70%,#262626 100%)}
.offer-box{left:152px;top:40px;width:290px;height:290px;background:linear-gradient(160deg,#3a3a3a 0%,#111 70%);border-radius:4px}
.offer-sparkle{left:760px;top:20px;width:420px;height:340px;border-radius:50%;background:radial-gradient(ellipse,rgba(220,220,220,.45) 0%,rgba(120,120,120,.15) 50%,rgba(0,0,0,0) 75%)}
.offer-text{left:436px;top:80px;width:480px;text-align:center;color:var(--white)}
.offer-text .kicker{font-size:22px;letter-spacing:1.5px}
.offer-text .big{font-size:42px;letter-spacing:1.5px;line-height:1.2}
.offer-text .sub{font-size:32px;letter-spacing:1.5px;line-height:1}
.offer .btn{left:566px;top:244px;width:158px;height:45px;color:var(--white)}

/* loose diamonds */
.loose-title{top:2313px}
.shape-grid{left:121px;top:2406px;width:962px;display:grid;grid-template-columns:repeat(5,179px);grid-auto-rows:243px;column-gap:17px;row-gap:16px}
.shape{border:1.5px solid var(--line);text-align:center;padding-top:38px}
.shape .cut{width:96px;height:110px;margin:0 auto;border-radius:8px;background:linear-gradient(160deg,#e9e9e9,#f7f7f7)}
.shape .label{margin-top:42px;font-size:17px;letter-spacing:1px;text-transform:uppercase}

/* testimonials */
.clients{top:2980px;left:0;width:1200px;height:386px;background:linear-gradient(135deg,#2b2b2b 0%,#111 35%,#262626 60%,#0b0b0b 100%);color:var(--white);text-align:center}
.clients .title{position:absolute;top:38px;width:100%;font-size:27px;letter-spacing:1px;text-transform:uppercase}
.clients .quote{position:absolute;left:290px;width:620px;top:108px;font-size:13px;line-height:1.45}
.clients .qmark{position:absolute;top:92px;font-size:60px;line-height:1;font-family:Georgia,serif}
.clients .name{position:absolute;top:165px;width:100%;font-size:27px;letter-spacing:1px;text-transform:uppercase}
.clients .stars{position:absolute;top:205px;width:100%;font-size:17px;color:var(--star);letter-spacing:2px}
.clients .dots{position:absolute;top:258px;left:580px;display:flex;gap:8px}
.clients .dots span{width:9px;height:9px;border-radius:50%;background:var(--white)}
.clients .dots span.off{background:transparent;border:1px solid var(--white)}
.clients .btn{left:521px;top:298px;width:158px;height:45px;color:var(--white)}

/* contact + about */
.col-title{top:3412px;font-size:27px;letter-spacing:1px;text-transform:uppercase;text-align:center}
.field{left:121px;width:478px;border:1.5px solid #9a9a9a;font-size:12px;color:#444;padding:10px 12px}
.submit{left:121px;top:3717px;width:478px;height:42px;background:var(--black);color:var(--white);font-size:13px;letter-spacing:1px;display:flex;align-items:center;justify-content:center}
.about-text{left:662px;top:3488px;width:386px;font-size:14px;line-height:1.35;text-align:center;color:#333}
.read-more{left:773px;top:3713px;width:158px;height:47px;color:var(--ink)}

/* footer */
.site-footer{top:3821px;left:0;width:1200px;height:317px;background:var(--black);color:var(--white)}
.f-head{top:55px;font-size:27px;text-transform:uppercase;letter-spacing:1px}
.f-list{font-size:12px;line-height:1.35}
.f-list li{list-style:none;display:flex;align-items:center;gap:8px}
.f-links li::before{content:"";width:4px;height:4px;border-radius:50%;background:var(--white);display:inline-block}
.news-input{left:902px;top:105px;width:178px;height:30px;border:1px solid var(--white);font-size:11px;padding:8px}
.news-btn{left:902px;top:144px;width:178px;height:26px;background:var(--white);color:var(--black);font-size:10px;display:flex;align-items:center;justify-content:center;text-transform:uppercase}
.socials{left:908px;top:190px;display:flex;gap:16px}
.socials span{width:14px;height:14px;border-radius:50%;background:var(--white)}
.f-rule{left:121px;top:242px;width:958px;height:1px;background:#333}
.copyright{left:121px;top:258px;font-size:12px}
.cards{left:930px;top:254px;display:flex;gap:6px}
.cards span{width:30px;height:21px;border-radius:3px;background:#d8d8d8}
</style>
</head>
<body>

<header class="site-header abs">
  <div class="menu abs">
    <svg width="18" height="14" viewBox="0 0 18 14"><path d="M0 1h18M0 7h18M0 13h18" stroke="#1a1a1a" stroke-width="2"/></svg>
    <span>MENU</span>
  </div>
  <div class="brand abs">
    <span class="brand-mark"></span>
    <span class="brand-name">Quillstone<br>Jewellers</span>
  </div>
  <div class="header-icons abs">
    <svg width="16" height="16" viewBox="0 0 16 16"><circle cx="6.5" cy="6.5" r="5" fill="none" stroke="#1a1a1a" stroke-width="1.8"/><path d="M10.5 10.5l4.5 4.5" stroke="#1a1a1a" stroke-width="1.8"/></svg>
    <svg width="16" height="16" viewBox="0 0 16 16"><circle cx="8" cy="5" r="3.5" fill="none" stroke="#1a1a1a" stroke-width="1.6"/><path d="M1.5 15.5c0-4 3-6 6.5-6s6.5 2 6.5 6" fill="none" stroke="#1a1a1a" stroke-width="1.6"/></svg>
    <svg width="17" height="16" viewBox="0 0 17 16"><path d="M8.5 15L2 8.5C0 6.5 0.5 2 4.2 1.5 6.2 1.2 7.6 2.5 8.5 3.8 9.4 2.5 10.8 1.2 12.8 1.5 16.5 2 17 6.5 15 8.5z" fill="none" stroke="#1a1a1a" stroke-width="1.6"/></svg>
    <svg width="18" height="16" viewBox="0 0 18 16"><path d="M0.5 1.5h3l2.2 9h9l2-6.5H5" fill="none" stroke="#1a1a1a" stroke-width="1.6"/><circle cx="7" cy="14" r="1.4" fill="#1a1a1a"/><circle cx="14" cy="14" r="1.4" fill="#1a1a1a"/></svg>
  </div>
</header>

<section class="hero abs">
  <div class="hero-gems abs" role="img" aria-label="Loose brilliant-cut diamonds on dark silk"></div>
  <div class="hero-frame abs">
    <div class="kicker">CERTIFIED</div>
    <div class="headline">LOOSE DIMONDS</div>
    <div class="amp">&amp;</div>
    <div class="headline">JEWELLERY</div>
  </div>
  <a class="btn">Shop Now</a>
</section>

<h2 class="section-title explore-title">Explore</h2>
<div class="category abs" style="left:87px"><div class="thumb" role="img" aria-label="Diamond engagement ring"></div><div class="label">Engegemnt Ring</div></div>
<div class="category abs" style="left:349px"><div class="thumb" role="img" aria-label="Diamond wedding band"></div><div class="label">Wedding Ring</div></div>
<div class="category abs" style="left:603px"><div class="thumb" role="img" aria-label="Diamond drop earrings"></div><div class="label">Diamond Earring</div></div>
<div class="category abs" style="left:860px"><div class="thumb" role="img" aria-label="Heart diamond pendant"></div><div class="label">Diamond Pendant</div></div>

<h2 class="section-title feature-title">Feature Products</h2>
<div class="tabs-line abs"></div>
<nav class="tabs abs"><span class="active">All</span><span>Latests</span><span>Best Seller</span><span>Discounted</span><span>Other</span></nav>
<div class="pager abs">‹ ›</div>

<article class="product abs" style="left:121px"><span class="tag">SAVE 55%</span><div class="photo" role="img" aria-label="Diamond halo ring in white gold"></div><div class="name">Product Name</div><div class="rule"></div><div class="price">$ 500.0</div></article>
<article class="product abs" style="left:452px"><span class="tag">SAVE 55%</span><div class="photo" role="img" aria-label="Cushion halo ring in yellow gold"></div><div class="name">Product Name</div><div class="rule"></div><div class="price">$ 500.0</div></article>
<article class="product abs" style="left:784px"><span class="tag">SAVE 55%</span><div class="photo" role="img" aria-label="Oval diamond ring in white gold"></div><div class="name">Product Name</div><div class="rule"></div><div class="price">$ 500.0</div></article>
<a class="btn browse">Brows More</a>

<section class="offer abs">
  <div class="offer-box abs" role="img" aria-label="Marquise diamond ring in an open gift box"></div>
  <div class="offer-sparkle abs" role="img" aria-label="Scattered loose diamonds on black silk"></div>
  <div class="offer-text abs">
    <div class="kicker">DISCOUNT OFFER</div>
    <div class="big">SAVE 30% OFF</div>
    <div class="sub">ON YOUR 1st OREDR</div>
  </div>
  <a class="btn">Shop Now</a>
</section>

<h2 class="section-title loose-title">Loose Diamonds</h2>
<div class="shape-grid abs">
  <div class="shape"><div class="cut" role="img" aria-label="Round cut diagram"></div><div class="label">Round</div></div>
  <div class="shape"><div class="cut" role="img" aria-label="Princess cut diagram"></div><div class="label">Princess</div></div>
  <div class="shape"><div class="cut" role="img" aria-label="Marquise cut diagram"></div><div class="label">Marquise</div></div>
  <div class="shape"><div class="cut" role="img" aria-label="Emerald cut diagram"></div><div class="label">Emerald</div></div>
  <div class="shape"><div class="cut" role="img" aria-label="Pear cut diagram"></div><div class="label">Pear</div></div>
  <div class="shape"><div class="cut" role="img" aria-label="Oval cut diagram"></div><div class="label">Oval</div></div>
  <div class="shape"><div class="cut" role="img" aria-label="Heart cut diagram"></div><div class="label">Heart</div></div>
  <div class="shape"><div class="cut" role="img" aria-label="Radiant cut diagram"></div><div class="label">Rediant</div></div>
  <div class="shape"><div class="cut" role="img" aria-label="Asscher cut diagram"></div><div class="label">Ascher</div></div>
  <div class="shape"><div class="cut" role="img" aria-label="Cushion cut diagram"></div><div class="label">Cushion</div></div>
</div>

<section class="clients abs">
  <div class="title">Our Clients Say`s</div>
  <div class="qmark" style="left:250px">“</div>
  <p class="quote">Lorem Ipsum is simply dummy text of the printing and typesetting industry. Lorem Ipsum has been the industry's standard dummy text ever since the 1500s.</p>
  <div class="qmark" style="left:915px">”</div>
  <div class="name">Mara Ellison</div>
  <div class="stars">★★★★★</div>
  <div class="dots"><span class="off"></span><span></span><span></span></div>
  <a class="btn">Brows More</a>
</section>

<h2 class="col-title abs" style="left:121px;width:478px">Contact Us</h2>
<div class="field abs" style="top:3493px;height:44px">Your Name</div>
<div class="field abs" style="top:3551px;height:40px">Email Address</div>
<div class="field abs" style="top:3606px;height:97px">Massage</div>
<a class="submit abs">SUBMIT NOW</a>

<h2 class="col-title abs" style="left:662px;width:386px">About Us</h2>
<p class="about-text abs">Lorem Ipsum is simply dummy text of the printing and typesetting industry. Lorem Ipsum has been the industry's standard dummy text ever since the 1500s, when an unknown printer took a galley of type and scrambled it to make a type specimen book. It has survived not only five centuries, but also the leap into electronic typesetting, remaining essentially unchanged. It was popularised in the 1960s with the release of Letraset sheets containing Lorem Ipsum passages, and more recently with desktop publishing software including versions of Lorem Ipsum.</p>
<a class="btn read-more">Read More</a>

<footer class="site-footer abs">
  <h3 class="f-head abs" style="left:121px">Contact</h3>
  <ul class="f-list abs" style="left:125px;top:106px">
    <li><svg width="10" height="10" viewBox="0 0 10 10"><path d="M2 0.5l2 2.5-1 1.2c.7 1.3 1.6 2.2 2.8 2.8l1.2-1 2.5 2-1.2 1.5C4.5 9.5 0.5 5.5.5 1.7z" fill="#fff"/></svg>(000) 555 0142</li>
    <li><svg width="10" height="10" viewBox="0 0 10 10"><path d="M2 0.5l2 2.5-1 1.2c.7 1.3 1.6 2.2 2.8 2.8l1.2-1 2.5 2-1.2 1.5C4.5 9.5 0.5 5.5.5 1.7z" fill="#fff"/></svg>(000) 555 0142</li>
    <li><svg width="10" height="10" viewBox="0 0 10 10"><path d="M2 0.5l2 2.5-1 1.2c.7 1.3 1.6 2.2 2.8 2.8l1.2-1 2.5 2-1.2 1.5C4.5 9.5 0.5 5.5.5 1.7z" fill="#fff"/></svg>(000) 555 0142</li>
    <li><svg width="10" height="8" viewBox="0 0 10 8"><rect width="10" height="8" fill="#fff"/><path d="M0 0l5 4 5-4" stroke="#000" fill="none"/></svg>info@quillstonejewellers.example</li>
    <li><svg width="10" height="12" viewBox="0 0 10 12"><path d="M5 12C5 12 0 7 0 4.5a5 5 0 0110 0C10 7 5 12 5 12z" fill="#fff"/><circle cx="5" cy="4.5" r="1.7" fill="#000"/></svg>24 Larkmoor Lane</li>
    <li style="padding-left:18px">Eastvale, MA 02999</li>
  </ul>

  <h3 class="f-head abs" style="left:399px">Quick Link</h3>
  <ul class="f-list f-links abs" style="left:415px;top:106px">
    <li>Home</li><li>Shop</li><li>Loose Diamonds</li><li>Education</li><li>Contact</li><li>About</li><li>Blog</li>
  </ul>

  <h3 class="f-head abs" style="left:645px">Timing</h3>
  <ul class="f-list abs" style="left:651px;top:106px">
    <li>Mon : 9:00 am – 5:30 pm</li><li>Tue : 9:00 am – 5:30 pm</li><li>Wed : 9:00 am – 5:30 pm</li><li>Thu : 9:00 am – 5:30 pm</li><li>Fri : 9:00 am – 5:30 pm</li><li>Sat : 9:00 am – 5:00 pm</li><li>Sun : 10:00 am – 5:00 pm</li>
  </ul>

  <h3 class="f-head abs" style="left:902px">Newsletter</h3>
  <div class="news-input abs">Email</div>
  <a class="news-btn abs">Subscribe Now</a>
  <div class="socials abs"><span></span><span></span><span></span><span></span><span></span><span></span></div>

  <div class="f-rule abs"></div>
  <p class="copyright abs">Copyright © 2017 Quillstone Jewellers - All Rights Reserved.</p>
  <div class="cards abs"><span></span><span></span><span></span><span></span><span></span></div>
</footer>

</body>
</html>
```